Quillmont Booking Engine Marketing Site

Hi,
I’m currently in the process of putting together a web application with the intention of providing small resorts/B&Bs/small hotels the ability to allow their customers to book online.
I’m looking to have a design created for a marketing site, to give potential customers additional information about my booking engine, as well as to help drive sign-ups. A lot of the competition out there appears outdated, so I would like something that is more modern and up to date.
I am looking for just the design (i’m a web developer, but I lack the creative skills for a good marketing site)
For some more background, I will be targeting business owners of smaller resorts and Bed & Breakfasts. These are typically family owned small businesses that may only have a 10 room setup. These businesses will also typically have additional amenities that they will have to rent out or sell to their clients ( ex. Spa, fruit basket, water sport rentals). My software will provide them with the ability to sell their amenities as well.
I’m open to different designs, but my main thing is I want it to look modern, and I want it to have several callouts to sign up for my product.
I am looking to have the homepage created, 1 interior page, and a style guide created (to show form fields, H1’s, etc.).
I had a logo created a couple months ago that will be included with this project brief.
If you need any additional information feel free to reach out to me.

Target Market(s)

This site will be targeted small business owners who are running small resorts, Bed and Breakfasts, or any business that provides rooms for their clients.

Industry/Entity Type

Saas

Number of Pages Required

2 page

Font styles to use
Sans Serif

Colors

Designer to choose colors to be used in the design.

Requirements
Must have
• A modern feel, with several CTA's that will drive to the registration page on the homepage. on the internal page, I mostly just need the page layout, I will reuse that page layout. and a style guide if at all possible (include colors, form fields, H1's, etc.)
Nice to have
• maybe a hero image at the top with buttons over the top? again i'm pretty open to most anything.
Should not have
• I like images, but I don't want the page overrun with images. A good balance.

```html
<!DOCTYPE html>
<html lang="en">
<head>
<meta charset="utf-8">
<title>Quillmont Booking Engine</title>
<link rel="stylesheet" href="https://fonts.googleapis.com/css2?family=Roboto:wght@400;500;700&display=swap">
<style>
:root{
  --green:#5cbf0e;
  --ink:#333;
  --heading:#4a4a4a;
  --muted:#7a7a7a;
  --sky-top:#82d6ef;
  --sky-bottom:#63a1e9;
  --line:#d4d4d4;
  --footer-bar:#f2f2f2;
  --ring:#f3f4f6;
  --white:#fff;
}
*{margin:0;padding:0;box-sizing:border-box}
html,body{width:712px;height:1200px;overflow:hidden}
body{font-family:"Roboto",sans-serif;color:var(--ink);background:var(--white);position:relative}
.abs{position:absolute}
.btn{position:absolute;background:var(--green);color:var(--white);font-size:8px;font-weight:500;text-transform:uppercase;display:flex;align-items:center;justify-content:center;letter-spacing:.2px}

/* Sign-up strip */
.signup-strip{top:0;left:0;width:712px;height:114px;overflow:hidden}
.signup-strip h2{position:absolute;left:80px;top:33px;font-size:18px;font-weight:500;line-height:22px;color:var(--heading)}

/* Benefits */
.benefits{top:114px;left:0;width:712px;height:306px;background:linear-gradient(180deg,var(--sky-top),var(--sky-bottom));overflow:hidden}
.benefits h2{position:absolute;left:80px;top:54px;font-size:21px;font-weight:500;color:var(--white)}
.benefit{position:absolute;display:flex;align-items:flex-start;gap:13px;color:var(--white);font-size:11.5px;line-height:15.5px;width:190px}
.benefit .icon{flex:none;width:26px;height:26px;border-radius:50%;background:var(--white);display:flex;align-items:center;justify-content:center}
.benefit p{margin-top:3px}
.app-preview{position:absolute;left:492px;top:74px;width:220px;height:232px;background:linear-gradient(160deg,rgba(255,255,255,.55),rgba(235,190,160,.55));border-radius:40px 0 0 0}

/* News */
.news-title{top:486px;left:0;width:712px;text-align:center;font-size:20px;font-weight:500;color:var(--heading)}
.card{position:absolute;top:547px;width:270px;height:232px;background:var(--white);box-shadow:0 2px 8px rgba(0,0,0,.09)}
.card .photo{height:125px;position:relative;overflow:hidden}
.card .date{position:absolute;left:0;top:0;width:40px;height:40px;background:var(--green);border-bottom-right-radius:40px;color:var(--white);padding:6px 0 0 9px}
.card .date b{display:block;font-size:12px;font-weight:500;line-height:12px}
.card .date span{font-size:6.5px;display:block}
.card h3{margin:16px 13px 4px;font-size:13px;font-weight:500;color:#222}
.card p{margin:0 13px;font-size:8.3px;line-height:12.6px;color:var(--muted)}
.card .more{display:flex;align-items:center;gap:6px;margin:7px 13px 0;font-size:8px;font-weight:500;color:var(--green)}

/* CTA band */
.cta-band{top:847px;left:0;width:712px;height:115px;background:linear-gradient(100deg,#6d7480,#8a8d92 45%,#9ea6ae 75%,#7c8792)}
.cta-band h2{position:absolute;left:80px;top:38px;font-size:20.5px;line-height:25px;font-weight:700;color:var(--white)}

/* Footer */
.brand{top:998px;left:80px;display:flex;align-items:center;gap:5px}
.brand .mark{width:16px;height:16px;border-radius:50%;background:var(--green)}
.brand .name{font-size:12px;font-weight:500;color:#2f5fa6;line-height:12px}
.brand .sub{display:block;font-size:6.5px;font-weight:400;color:#2f5fa6;letter-spacing:.3px}
.about{top:1028px;left:80px;width:160px;font-size:8px;line-height:12.5px;color:var(--muted)}
.social{top:1074px;left:80px;display:flex;gap:10px}
.social span{width:6px;height:6px;border-radius:50%;background:#8a8a8a}
.contact{left:268px;font-size:8px;line-height:10px;color:var(--muted);display:flex;gap:7px}
.field{position:absolute;border:1px solid var(--line);font-size:7px;color:var(--muted);padding:5px 9px}
.footer-bar{top:1154px;left:0;width:712px;height:46px;background:var(--footer-bar)}
.footer-bar .copy{position:absolute;left:80px;top:18px;font-size:8px;color:var(--muted)}
.footer-bar nav{position:absolute;right:80px;top:18px;display:flex;gap:25px;font-size:7.5px;color:#555;text-transform:uppercase}
</style>
</head>
<body>

<section class="abs signup-strip">
  <svg class="abs" style="left:0;top:0" width="712" height="114" aria-hidden="true">
    <circle cx="20" cy="80" r="60" fill="none" stroke="var(--ring)" stroke-width="20"/>
    <circle cx="445" cy="0" r="42" fill="none" stroke="var(--ring)" stroke-width="12"/>
    <circle cx="712" cy="120" r="40" fill="none" stroke="var(--ring)" stroke-width="12"/>
  </svg>
  <h2>Sign Up Today - Increase Your<br>Customer Traffic</h2>
  <a class="btn" style="left:518px;top:46px;width:114px;height:21px">Sign Up</a>
</section>

<section class="abs benefits">
  <h2>Benefits</h2>
  <div class="benefit" style="left:80px;top:110px"><span class="icon"><svg width="12" height="10"><circle cx="3" cy="3" r="2" fill="#7fb2ea"/><circle cx="9" cy="3" r="2" fill="#7fb2ea"/><rect x="0" y="6" width="12" height="4" rx="2" fill="#7fb2ea"/></svg></span><p>Ideal For Small<br>Business</p></div>
  <div class="benefit" style="left:268px;top:110px"><span class="icon"><svg width="12" height="9"><path d="M1 8 L6 1 L11 8 Z" fill="#7fb2ea"/></svg></span><p>Ability to Sell Your<br>Amenities</p></div>
  <div class="benefit" style="left:80px;top:165px"><span class="icon"><svg width="10" height="12"><rect x="1" y="3" width="8" height="9" rx="3" fill="#7fb2ea"/><rect x="3" y="0" width="4" height="3" fill="#7fb2ea"/></svg></span><p>It Saves a Lot of Money<br>and Efforts</p></div>
  <div class="benefit" style="left:268px;top:165px"><span class="icon"><svg width="11" height="11"><circle cx="2" cy="5.5" r="1.8" fill="#7fb2ea"/><circle cx="9" cy="2" r="1.8" fill="#7fb2ea"/><circle cx="9" cy="9" r="1.8" fill="#7fb2ea"/><path d="M2 5.5 L9 2 M2 5.5 L9 9" stroke="#7fb2ea"/></svg></span><p>Get Deeper Knowledge of<br>Your Business</p></div>
  <div class="benefit" style="left:80px;top:220px"><span class="icon"><svg width="12" height="9"><rect x="0.5" y="0.5" width="11" height="8" rx="1" fill="none" stroke="#7fb2ea"/><rect x="0.5" y="2.5" width="11" height="2" fill="#7fb2ea"/></svg></span><p>Payments are Easier<br>and Faster</p></div>
  <div class="benefit" style="left:268px;top:220px"><span class="icon"><svg width="12" height="12"><circle cx="6" cy="6" r="5.5" fill="#7fb2ea"/><path d="M6 3 V6 H8.5" stroke="#fff" fill="none"/></svg></span><p>It Works 24/7 all Around<br>the World</p></div>
  <div class="app-preview" role="img" aria-label="Hand holding a smartphone showing the booking engine with hotel room listings"></div>
</section>

<h2 class="abs news-title">News and Updates</h2>

<article class="card" style="left:80px">
  <div class="photo" role="img" aria-label="City skyline with a lit bridge at dusk" style="background:linear-gradient(180deg,#5c5a8a,#b0608a 55%,#3a3550)">
    <div class="date"><b>01</b><span>JAN</span></div>
  </div>
  <h3>Lorem ipsum dolor</h3>
  <p>Lorem ipsum dolor sit amet, con sectet iscing elit, sed do eiusm od tetmpor ididunt ut labore et dolore magna aliqua. Sed ut perspiciatis unde omnis iste natus error sit voluptatem</p>
  <div class="more">READ MORE <svg width="5" height="7"><path d="M1 1 L4 3.5 L1 6" stroke="var(--green)" fill="none"/></svg></div>
</article>

<article class="card" style="left:362px">
  <div class="photo" role="img" aria-label="Woman smiling at her phone against a blurred city background" style="background:linear-gradient(90deg,#c9d3dc,#a99a90 55%,#d5dae0)">
    <div class="date"><b>07</b><span>JAN</span></div>
  </div>
  <h3>Lorem ipsum dolor</h3>
  <p>Lorem ipsum dolor sit amet, con sectet iscing elit, sed do eiusm od tetmpor ididunt ut labore et dolore magna aliqua. Sed ut perspiciatis unde omnis iste natus error sit voluptatem</p>
  <div class="more">READ MORE <svg width="5" height="7"><path d="M1 1 L4 3.5 L1 6" stroke="var(--green)" fill="none"/></svg></div>
</article>

<section class="abs cta-band" role="img" aria-label="Blurred breakfast tray on a hotel bed">
  <h2>Grow Your Small Business With<br>Quillmont Booking</h2>
  <a class="btn" style="left:518px;top:47px;width:114px;height:21px">Sign Up</a>
</section>

<div class="abs brand"><span class="mark"></span><span class="name">QUILLMONT<span class="sub">BOOKING ENGINE</span></span></div>
<p class="abs about">Lorem ipsum dolor sit amet, consectetur adipiscing elit, sed do eiusmod tempor incididunt ut labore</p>
<div class="abs social"><span></span><span></span><span></span><span></span></div>

<div class="abs contact" style="top:998px"><svg width="7" height="10"><path d="M3.5 10 C1 6 0 4.5 0 3.5 A3.5 3.5 0 0 1 7 3.5 C7 4.5 6 6 3.5 10Z" fill="var(--green)"/></svg><span>Unit 4, Larkfield Court, Brenmoor,<br>BR7 2LQ.</span></div>
<div class="abs contact" style="top:1034px"><svg width="9" height="7"><rect width="9" height="7" fill="var(--green)"/><path d="M0 0 L4.5 4 L9 0" stroke="#fff" fill="none"/></svg><span>hello@quillmont.test</span></div>
<div class="abs contact" style="top:1064px"><svg width="8" height="8"><path d="M1 0 L3 2 L2 3.5 C3 5 4 6 4.5 6 L6 5 L8 7 L6.5 8 C3 8 0 5 0 1.5Z" fill="var(--green)"/></svg><span>+(00)555 - 014 - 2286</span></div>

<div class="field" style="left:408px;top:998px;width:108px;height:19px">Your Name</div>
<div class="field" style="left:524px;top:998px;width:108px;height:19px">Your Email</div>
<div class="field" style="left:408px;top:1025px;width:224px;height:19px">Subject</div>
<div class="field" style="left:408px;top:1052px;width:224px;height:47px">Mesage</div>
<a class="btn" style="left:468px;top:1110px;width:104px;height:15px;font-size:7px">Submit</a>

<footer class="abs footer-bar">
  <span class="copy">©2018 All Rights Reserved</span>
  <nav><span>Home</span><span>How it works</span><span>About</span><span>Interior</span><span>Contact Us</span></nav>
</footer>

</body>
</html>
```